Boat business cards

I'm looking for business cards with the two logos I've attached. I don't have an specific idea in mind and open to anything. All the usual info will be on the card. Name, position in company, nr, email, address, ect. The company rents out these two boats for charters and fishing.

```html
<!DOCTYPE html>
<html lang="en">
<head>
<meta charset="utf-8">
<title>Harbor Star &amp; Sea Ready – Business Cards</title>
<link href="https://fonts.googleapis.com/css2?family=Montserrat:wght@400;500;600;700&display=swap" rel="stylesheet">
<style>
  :root {
    --teal: #1f4452;
    --tan: #9a8465;
    --white: #ffffff;
    --ink: #111111;
    --hull-light: #c9b48f;
    --hull-blue: #8ea3cf;
  }
  * { box-sizing: border-box; margin: 0; padding: 0; }
  html, body { width: 1200px; height: 1200px; overflow: hidden; background: var(--white); }
  body { position: relative; font-family: 'Montserrat', sans-serif; }

  .card { position: absolute; left: 122px; width: 963px; height: 540px; overflow: hidden; }
  .card--front { top: 37px; background: var(--teal); }
  .card--back { top: 631px; background: var(--white); border: 1px solid #d7d7d7; }

  /* front */
  .yacht-art {
    position: absolute; left: 228px; top: 161px; width: 521px; height: 142px;
    border-radius: 6px;
    background: linear-gradient(180deg, #e9ecef 0%, #e9ecef 40%, var(--hull-light) 60%, #8aa6d2 100%);
    opacity: .85;
  }
  .brand-front {
    position: absolute; left: 0; right: 0; top: 300px;
    text-align: center; color: var(--white);
    font-weight: 700; font-size: 50px; letter-spacing: 2px; text-transform: uppercase;
  }
  .web-band { position: absolute; left: 0; top: 447px; width: 963px; height: 50px; }
  .web-link {
    position: absolute; left: 0; right: 0; top: 447px; height: 50px;
    display: flex; align-items: center; justify-content: center; gap: 10px;
    color: var(--white); font-size: 27px; font-weight: 500;
  }
  .web-link svg { width: 36px; height: 36px; }

  /* back */
  .wave { position: absolute; left: 0; top: 0; width: 963px; height: 540px; }
  .boat-art {
    position: absolute; left: 70px; top: 28px; width: 372px; height: 166px;
    border-radius: 6px;
    background: linear-gradient(180deg, #eef0f3 0%, #eef0f3 50%, var(--hull-blue) 100%);
  }
  .brand-back {
    position: absolute; left: 82px; top: 188px;
    color: #3a3a3a; font-weight: 700; font-size: 42px;
  }
  .person { position: absolute; right: 56px; top: 48px; text-align: right; color: var(--ink); }
  .person__name { font-size: 44px; font-weight: 700; line-height: 1.05; }
  .person__role { font-size: 31px; font-weight: 500; margin-top: 2px; }
  .name-tab { position: absolute; left: 924px; top: 58px; width: 39px; height: 71px; background: var(--teal); }

  .contact { position: absolute; display: flex; align-items: center; gap: 12px; color: var(--white); font-size: 29px; font-weight: 500; }
  .contact .icon {
    width: 42px; height: 42px; border-radius: 50%; background: var(--white);
    display: flex; align-items: center; justify-content: center; flex: none;
  }
  .contact .icon svg { width: 24px; height: 24px; }
  .contact--phone { left: 38px; top: 341px; }
  .contact--mail { left: 38px; top: 399px; }
  .contact--social { left: 38px; top: 458px; }
  .contact--address { left: 566px; top: 398px; align-items: flex-start; line-height: 36px; }
  .contact--address .icon { margin-top: 0; }
</style>
</head>
<body>

<section class="card card--front">
  <div class="yacht-art" role="img" aria-label="Illustration of a white and tan motor yacht on the water"></div>
  <div class="brand-front">Harbor Star</div>
  <svg class="web-band" viewBox="0 0 963 50" aria-hidden="true">
    <rect x="0" y="0" width="963" height="50" fill="var(--white)"/>
    <polygon points="256,0 706,0 682,25 706,50 256,50 280,25" fill="var(--tan)"/>
  </svg>
  <div class="web-link">
    <svg viewBox="0 0 36 36" aria-hidden="true">
      <circle cx="18" cy="18" r="17" fill="var(--white)"/>
      <g fill="none" stroke="var(--ink)" stroke-width="1.6">
        <circle cx="18" cy="18" r="11"/>
        <ellipse cx="18" cy="18" rx="5" ry="11"/>
        <line x1="7" y1="18" x2="29" y2="18"/>
        <line x1="9" y1="12" x2="27" y2="12"/>
        <line x1="9" y1="24" x2="27" y2="24"/>
      </g>
    </svg>
    <span>yourwebsite.com</span>
  </div>
</section>

<section class="card card--back">
  <svg class="wave" viewBox="0 0 963 540" aria-hidden="true">
    <path d="M0,194 C90,255 200,302 330,306 C510,300 720,238 963,238 L963,540 L0,540 Z" fill="var(--tan)"/>
    <path d="M0,222 C90,268 200,300 330,292 C510,282 720,242 963,244 L963,540 L0,540 Z" fill="var(--teal)"/>
  </svg>
  <div class="boat-art" role="img" aria-label="Illustration of a blue center-console fishing boat with tower"></div>
  <div class="brand-back">Sea Ready</div>

  <div class="person">
    <div class="person__name">Your Name</div>
    <div class="person__role">Manager</div>
  </div>
  <div class="name-tab"></div>

  <div class="contact contact--phone">
    <span class="icon"><svg viewBox="0 0 24 24"><path d="M6.6 2.5l3 3.2-1.8 2.3c1.1 2.5 3.3 4.9 6.1 6.3l2.2-1.9 3.4 2.9-1.6 3.6c-7.8-.6-13.7-6.8-14.3-14.4z" fill="var(--ink)"/></svg></span>
    <span>000-123-456</span>
  </div>
  <div class="contact contact--mail">
    <span class="icon"><svg viewBox="0 0 24 24"><rect x="3" y="6" width="18" height="12" rx="1" fill="var(--ink)"/><path d="M3.5 6.5l8.5 6.5 8.5-6.5M3.5 17.5l6-5.5M20.5 17.5l-6-5.5" stroke="var(--white)" stroke-width="1.4" fill="none"/></svg></span>
    <span>yourname@example.com</span>
  </div>
  <div class="contact contact--social">
    <span class="icon"><svg viewBox="0 0 24 24"><circle cx="12" cy="12" r="7" fill="var(--ink)"/></svg></span>
    <span>yourname</span>
  </div>
  <div class="contact contact--address">
    <span class="icon"><svg viewBox="0 0 24 24"><path d="M12 2.5a6.5 6.5 0 0 0-6.5 6.5c0 4.6 6.5 12.5 6.5 12.5s6.5-7.9 6.5-12.5A6.5 6.5 0 0 0 12 2.5z" fill="var(--ink)"/><circle cx="12" cy="9" r="2.4" fill="var(--white)"/></svg></span>
    <span>House, street name<br>city, Country 123</span>
  </div>
</section>

</body>
</html>
```